Brochure for a civil enineering company in A4 format

I need a brochure design for our company VELTA Engineering S.r.l.. We are an engineering consultant company. Our main clients are from the infrastructure industry (geotechnical and underground sectors mainly).
We are looking for a 2 pages (4 faces) fold out design with a glued pocket where we can put individual data sheets.
I need A4 format pages.

Target Market(s)

We are an engineering consultant company. Our main clients are from the infrastructure industry (geotechnical and underground sectors mainly).

Industry/Entity Type

Civil Engineer

Font styles to use
Sans Serif

Requirements
Must have
• Overall: 2 pages in A4 format
Essential style. Bright and modern appearance.
Glued pocket
Logo integrated in a picture on the pocket where I would like to insert a slogan (… velta engineering … reliable solutions …)
Attached are selected images which the designer can use and edit at their own discretion.
Some advice in the following (anyway designers are free to provide their solutions):
Outer sheets:
Front page with name, logo. It could be nice to have the “m” of the logo integrated in a pictures, also a modified picture (I mean modify one of the attached pictures) so to create a general image and do not tie the cover to a specific job.
Back page: offices address and info@velta-eng.example address. Nice to have one space for a slogan.
Inner sheet: text that I upload in the file “inside-sheets”, possibly with pictures on each sheet. In the right faces insert the glued pocket. On this pages insert the section OUR EXPERIENCE ….with a space for a picture of our team.
Nice to have
• Clean and essential design.
Pictures choosing from the atteched ones. Pictures could be modified in a very light manner to make them a general idea of the work ( I mean geotechnical world) without to be immediately linked to a specific site.
Should not have
• excessive frills

```html
<!DOCTYPE html>
<html lang="en">
<head>
<meta charset="utf-8">
<title>VELTA Engineering – Brochure</title>
<link href="https://fonts.googleapis.com/css2?family=Montserrat:wght@400;600;700&family=Open+Sans:wght@400;600&display=swap" rel="stylesheet">
<style>
  :root{
    --stage:#ececec;
    --paper:#ffffff;
    --ink:#2b2b2b;
    --ink-soft:#6a6a6a;
    --accent:#4f6a3c;
    --photo-earth-a:#8c8a7c;
    --photo-earth-b:#b9b4a3;
    --photo-green-a:#3f5236;
    --photo-green-b:#7f8c6c;
    --photo-team-a:#d9d9d9;
    --photo-team-b:#bfb6ab;
  }
  *{box-sizing:border-box;margin:0;padding:0}
  html,body{width:1200px;height:2392px;overflow:hidden}
  body{background:var(--stage);font-family:"Open Sans",Arial,sans-serif;color:var(--ink);position:relative}

  .spread{position:absolute;left:60px;width:1080px;height:764px;display:flex;box-shadow:0 6px 24px rgba(0,0,0,.12)}
  .spread--outer{top:372px}
  .spread--inner{top:1256px}
  .page{position:relative;width:540px;height:764px;background:var(--paper);overflow:hidden}
  .page + .page{border-left:1px solid #e2e2e2}

  .brand-name{font-family:"Montserrat",Arial,sans-serif;font-weight:600;color:var(--ink);letter-spacing:-1px;display:flex;align-items:center;gap:8px}
  .brand-name .dot{width:10px;height:10px;border-radius:50%;background:var(--accent)}

  /* back page */
  .back-brand{position:absolute;left:64px;top:300px;font-size:30px}
  .contact{position:absolute;left:64px;top:352px;font-size:9px;line-height:1.55;color:var(--ink-soft)}
  .contact .label{font-family:"Montserrat",Arial,sans-serif;font-weight:700;color:var(--ink);font-size:9px;margin-top:10px}
  .contact .company{font-weight:600;color:var(--ink)}

  /* front page */
  .front-photo{position:absolute;inset:0}
  .front-brand{position:absolute;left:150px;top:346px;font-size:56px;background:var(--paper);padding:6px 18px;border-radius:40px}

  /* inner left */
  .hero-photo{position:absolute;left:0;top:0;width:540px;height:330px}
  .hero-text{position:absolute;left:40px;top:36px;width:230px;color:#fff}
  .section-title{font-family:"Montserrat",Arial,sans-serif;font-weight:700;font-size:12px;letter-spacing:1px;text-transform:uppercase;color:var(--accent);margin-bottom:8px}
  .hero-text .section-title{color:#fff}
  .hero-text p{font-size:9px;line-height:1.6}
  .badge-photo{position:absolute;left:440px;top:270px;width:130px;height:130px}
  .services{position:absolute;left:40px;top:410px;width:380px}
  .services p{font-size:9.5px;line-height:1.6;color:var(--ink-soft);margin-bottom:12px}
  .services ul{list-style:none}
  .services li{font-size:9.5px;line-height:1.5;color:var(--ink-soft);padding-left:16px;position:relative;margin-bottom:12px}
  .services li::before{content:"";position:absolute;left:0;top:5px;width:6px;height:6px;background:var(--accent)}

  /* inner right */
  .team-photo{position:absolute;right:0;top:0;width:340px;height:190px}
  .experience{position:absolute;left:40px;top:214px;width:460px}
  .experience h2{font-family:"Montserrat",Arial,sans-serif;font-weight:700;font-size:12px;letter-spacing:1px;text-transform:uppercase;color:var(--accent);margin-bottom:12px}
  .columns{display:flex;gap:26px}
  .columns > div{flex:1}
  .columns p{font-size:9.5px;line-height:1.65;color:var(--ink-soft);margin-bottom:10px}
  .footer-photo{position:absolute;left:0;bottom:0;width:540px;height:200px}
</style>
</head>
<body>

<section class="spread spread--outer">
  <article class="page page--back">
    <div class="brand-name back-brand"><span class="dot"></span>velta</div>
    <address class="contact">
      <div class="company">VELTA Engineering S.r.l.</div>
      <div class="label">Head office</div>
      <div>Via Roma 12</div>
      <div>20121 Milano, Italy</div>
      <div class="label">Branch office</div>
      <div>Corso Francia 8</div>
      <div>10138 Torino, Italy</div>
      <div class="label">Contact</div>
      <div>info@velta-eng.example</div>
      <div>+39 02 0000 1234</div>
    </address>
  </article>

  <article class="page page--front">
    <svg class="front-photo" viewBox="0 0 540 764" role="img" aria-label="Cover photograph of geotechnical and construction sites seen from above">
      <defs>
        <linearGradient id="coverPhoto" x1="0" y1="0" x2="1" y2="1">
          <stop offset="0" stop-color="var(--photo-earth-b)"/>
          <stop offset="1" stop-color="var(--photo-earth-a)"/>
        </linearGradient>
      </defs>
      <path d="M250 0 H540 V764 H250 C120 640 120 120 250 0 Z" fill="url(#coverPhoto)"/>
      <path d="M250 0 C120 120 120 640 250 764" fill="none" stroke="#ffffff" stroke-width="14"/>
    </svg>
    <div class="brand-name front-brand">velta</div>
  </article>
</section>

<section class="spread spread--inner">
  <article class="page page--company">
    <svg class="hero-photo" viewBox="0 0 540 330" role="img" aria-label="Photograph of a hillside site with excavation works, green-grey tones">
      <defs>
        <linearGradient id="heroPhoto" x1="0" y1="0" x2="1" y2="1">
          <stop offset="0" stop-color="var(--photo-green-a)"/>
          <stop offset="1" stop-color="var(--photo-green-b)"/>
        </linearGradient>
      </defs>
      <rect width="540" height="330" fill="url(#heroPhoto)"/>
    </svg>
    <div class="hero-text">
      <h2 class="section-title">Our company</h2>
      <p>VELTA Engineering is an independent consultancy supporting owners and contractors in geotechnical and underground works across Europe.</p>
    </div>
    <svg class="badge-photo" viewBox="0 0 130 130" role="img" aria-label="Round photograph of a tunnel portal">
      <defs>
        <radialGradient id="badgePhoto">
          <stop offset="0" stop-color="#3a3a36"/>
          <stop offset="1" stop-color="var(--photo-earth-a)"/>
        </radialGradient>
      </defs>
      <circle cx="65" cy="65" r="60" fill="url(#badgePhoto)" stroke="#ffffff" stroke-width="8"/>
    </svg>
    <div class="services">
      <h2 class="section-title">Our services</h2>
      <p>We provide design, assessment and site support from feasibility to completion.</p>
      <ul>
        <li>Geotechnical investigation and ground modelling</li>
        <li>Tunnel and shaft design for conventional and mechanised excavation</li>
        <li>Slope stability, retaining structures and foundations</li>
        <li>Monitoring plans and back analysis during construction</li>
        <li>Independent checking and technical due diligence</li>
      </ul>
    </div>
  </article>

  <article class="page page--experience">
    <svg class="team-photo" viewBox="0 0 340 190" role="img" aria-label="Team photograph of the company's engineers">
      <defs>
        <linearGradient id="teamPhoto" x1="0" y1="0" x2="1" y2="0">
          <stop offset="0" stop-color="var(--photo-team-a)"/>
          <stop offset="1" stop-color="var(--photo-team-b)"/>
        </linearGradient>
      </defs>
      <rect width="340" height="190" fill="url(#teamPhoto)"/>
    </svg>
    <div class="experience">
      <h2>Our experience and expertise</h2>
      <div class="columns">
        <div>
          <p>Our team brings together engineers with long experience in tunnelling, deep excavations and ground improvement. We work side by side with clients to turn complex ground conditions into safe, efficient and reliable solutions.</p>
          <p>Projects include metro lines, road and rail tunnels, hydropower caverns and urban shafts, where careful analysis and clear reporting support every decision on site.</p>
        </div>
        <div>
          <p>Each assignment is followed by a senior engineer from start to finish, keeping communication direct and results consistent.</p>
          <p>We combine numerical modelling with practical site knowledge to deliver designs that are robust, economical and easy to build.</p>
        </div>
      </div>
    </div>
    <svg class="footer-photo" viewBox="0 0 540 200" role="img" aria-label="Photograph of a road cut through hills with retaining works">
      <defs>
        <linearGradient id="footerPhoto" x1="0" y1="0" x2="1" y2="1">
          <stop offset="0" stop-color="var(--photo-green-b)"/>
          <stop offset="1" stop-color="var(--photo-earth-a)"/>
        </linearGradient>
      </defs>
      <path d="M0 120 C180 40 360 30 540 60 V200 H0 Z" fill="url(#footerPhoto)"/>
    </svg>
  </article>
</section>

</body>
</html>
```